One Page / Executive Summary for Silverpine Executive Search

We would need an executive summary for our firm Silverpine Executive Search - like a small one pager which we can via PDF to our clients.
It should include like the file 23030 all Infos - Only Track Record needs to be complemented
But it should be designed much nicer than it is now - also open for new design situations but it should fit our website concept www.silverpinexs.io
It should also include a graph of the recruiting process - maybe draw a new one.?
We would need a very elegant, modern, slim design, it should look very female - it should not have a green color block on the top but be more sleek bright and with our bird
Target Market(s)
CEO, HR executives
Industry/Entity Type
HR Consultantcy
Other font styles liked:
- Calibri, cost or robotic condensed
Requirements
Must have
- sleek slim modern elegant design, ideally a white side with a frame or with our bird
Nice to have
- project progress on our website, female modern, elegant design, not too overloaded, possibility to complement our text
Should not have
- no petrol color block as on our website or as in our proposal, prefer a white background with our photo as a log,

```html
<!DOCTYPE html>
<html lang="en">
<head>
<meta charset="utf-8">
<title>Silverpine Executive Search – Executive Summary</title>
<link href="https://fonts.googleapis.com/css2?family=Josefin+Sans:wght@200;300&family=Roboto+Condensed:wght@300;400;700&family=Raleway:wght@300&display=swap" rel="stylesheet">
<style>
:root{
  --petrol:#064b5f;
  --teal:#1a98b4;
  --sky:#56b1c9;
  --red:#e33b2e;
  --ink:#164b61;
  --muted:#3d7a90;
  --white:#ffffff;
}
*{margin:0;padding:0;box-sizing:border-box}
html,body{width:848px;height:1200px;overflow:hidden;background:var(--white)}
body{font-family:"Roboto Condensed",Arial,sans-serif;color:var(--ink);font-weight:300}
.page{position:relative;width:848px;height:1200px}
.abs{position:absolute}

.brand-tile{left:51px;top:0;width:134px;height:158px;background:var(--petrol);border-radius:0 0 12px 12px;box-shadow:0 3px 8px rgba(0,0,0,.18);display:flex;align-items:center;justify-content:center}
.brand-tile span{color:var(--white);font-family:"Roboto Condensed",sans-serif;font-weight:400;font-size:19px;letter-spacing:1px}

.title{left:305px;top:42px;font-family:"Josefin Sans",sans-serif;font-weight:200;font-size:56px;letter-spacing:9px;color:var(--petrol);line-height:1}
.title-rule{left:307px;top:101px;width:39px;height:2px;background:var(--red)}
.tagline{left:307px;top:110px;font-family:"Raleway",sans-serif;font-weight:300;font-size:17px;line-height:25px;color:var(--muted)}

.divider{left:281px;top:193px;height:858px;border-left:3px dotted var(--teal)}

.heading{font-weight:700;color:var(--red);font-size:19.5px;line-height:22px;text-transform:uppercase}
.sub{font-weight:700;color:var(--petrol);font-size:16.5px;line-height:19px}
.body{font-size:15.5px;line-height:18.8px;color:var(--ink)}

.industry{left:50px;display:flex;align-items:center;gap:14px;font-size:14.5px;line-height:17px;font-weight:400;color:var(--petrol)}
.industry svg{width:32px;height:32px;flex:none}

.portrait{width:104px;height:104px;border-radius:50%;background:radial-gradient(circle at 50% 40%,#e9c7ad 0 18%,#1a98b4 19%);overflow:hidden}
.portrait::after{content:"";position:absolute;left:22px;top:68px;width:60px;height:50px;border-radius:50% 50% 0 0;background:#111}
.portrait-name{font-size:14px;line-height:17px;color:var(--ink)}

.stat{left:51px;display:flex;align-items:center;gap:19px}
.stat-badge{width:38px;height:38px;border-radius:8px;background:var(--teal);color:var(--white);font-weight:700;font-size:15px;display:flex;align-items:center;justify-content:center;flex:none}
.stat-label{font-size:14.5px;line-height:17px;font-weight:400;color:var(--petrol)}
.stat-label small{display:block;font-size:13px;font-weight:300}

.cities{left:109px;top:984px;font-size:14.5px;line-height:17px}

.values{left:307px;top:431px;width:541px;height:53px;background:var(--sky);border-radius:18px 0 0 18px;color:var(--white);font-weight:700;font-size:18.5px;letter-spacing:2.6px;padding:14px 0 0 21px}

.why{left:307px;top:536px;width:480px;list-style:none}
.why li{position:relative;padding-left:27px;font-size:15.5px;line-height:18.8px}
.why li::before{content:"•";position:absolute;left:0;font-size:10px;color:var(--ink)}

.step{top:760px;width:153px;height:172px;background:var(--white);border-radius:12px;box-shadow:0 3px 8px rgba(0,0,0,.12)}
.step-head{height:55px;border-radius:12px 12px 0 0;color:var(--white);font-weight:700;font-size:13.5px;line-height:17px;text-align:center;display:flex;align-items:center;justify-content:center;padding-top:4px}
.step-num{position:absolute;left:64px;top:-11px;width:25px;height:25px;border-radius:50%;background:var(--white);border:1.5px solid var(--teal);color:var(--petrol);font-size:15px;font-weight:400;text-align:center;line-height:22px}
.step-body{padding:6px 6px 0 10px}
.step-body b{display:block;font-weight:700;color:var(--petrol);font-size:11px;line-height:13px;margin-top:4px}
.step-body p{font-size:10.5px;line-height:13.5px;color:var(--muted);margin-bottom:4px}

.track{left:315px;top:983px;width:470px;font-size:15.3px;line-height:17px}

.footer{left:0;top:1067px;width:788px;height:92px;background:var(--sky);border-radius:0 18px 18px 0}
.cta{left:53px;top:1078px;color:var(--white);font-weight:700;font-size:29px;line-height:35px}
.contact{left:307px;display:flex;align-items:center;gap:9px;color:var(--white);font-size:14.5px}
.contact svg{width:20px;height:20px}
.social{top:1093px;width:32px;height:32px;border-radius:50%;background:var(--white)}
.badge{left:713px;top:1082px;width:62px;height:62px;border-radius:50%;background:var(--white);display:flex;align-items:center;justify-content:center;color:var(--petrol);font-size:11px;font-weight:400}
</style>
</head>
<body>
<div class="page">

  <div class="abs brand-tile"><span>Silverpine</span></div>

  <h1 class="abs title">SILVERPINE</h1>
  <div class="abs title-rule"></div>
  <p class="abs tagline">So, they don’t wear ties in the boardroom anymore.<br>We never did...</p>

  <div class="abs divider"></div>

  <!-- Left column -->
  <h2 class="abs heading" style="left:51px;top:196px">What we do</h2>
  <p class="abs body" style="left:51px;top:222px;width:225px">While we consider ourselves a boutique Executive Search Firm, our span across Europe and covers multiple industries:</p>

  <div class="abs industry" style="top:319px">
    <svg viewBox="0 0 32 32"><circle cx="16" cy="16" r="16" fill="#1a98b4"/><rect x="13" y="7" width="6" height="18" rx="1" fill="#fff"/><rect x="7" y="13" width="18" height="6" rx="1" fill="#fff"/></svg>
    <span>HEALTHCARE</span>
  </div>
  <div class="abs industry" style="top:364px">
    <svg viewBox="0 0 32 32"><circle cx="16" cy="16" r="16" fill="#1a98b4"/><polyline points="5,22 11,15 16,19 25,10" fill="none" stroke="#fff" stroke-width="2.2"/><polyline points="20,10 25,10 25,15" fill="none" stroke="#fff" stroke-width="2.2"/></svg>
    <span>PRIVATE EQUITY &amp;<br>VENTURE CAPITAL</span>
  </div>
  <div class="abs industry" style="top:411px">
    <svg viewBox="0 0 32 32"><circle cx="16" cy="16" r="16" fill="#1a98b4"/><circle cx="10" cy="11" r="3" fill="#fff"/><circle cx="16" cy="9" r="3.4" fill="#fff"/><circle cx="22" cy="11" r="3" fill="#fff"/><rect x="7" y="15" width="6" height="11" rx="3" fill="#fff"/><rect x="13" y="14" width="6" height="13" rx="3" fill="#fff"/><rect x="19" y="15" width="6" height="11" rx="3" fill="#fff"/></svg>
    <span>CONSUMER</span>
  </div>
  <div class="abs industry" style="top:458px">
    <svg viewBox="0 0 32 32"><circle cx="16" cy="16" r="16" fill="#1a98b4"/><path d="M7 10h8v13H7zM17 10h8v13h-8z" fill="none" stroke="#fff" stroke-width="1.6"/><path d="M9 14h4M9 17h4M19 14h4M19 17h4" stroke="#fff" stroke-width="1"/></svg>
    <span>EDUCATION &amp;<br>ADMINISTRATION</span>
  </div>

  <h2 class="abs heading" style="left:50px;top:508px">Managing Directors</h2>
  <div class="abs portrait" style="left:51px;top:538px" role="img" aria-label="Portrait photo of managing director Dr. Clara Vennholt-Berger"></div>
  <div class="abs portrait" style="left:165px;top:536px" role="img" aria-label="Portrait photo of managing director Marie Castell"></div>
  <p class="abs portrait-name" style="left:53px;top:642px">Dr. Clara<br>Vennholt-Berger</p>
  <p class="abs portrait-name" style="left:185px;top:647px">Marie Castell</p>

  <h2 class="abs heading" style="left:50px;top:721px">By the numbers</h2>
  <div class="abs stat" style="top:752px"><div class="stat-badge">95%</div><div class="stat-label">PLACEMENT<br>RATE</div></div>
  <div class="abs stat" style="top:799px"><div class="stat-badge">##</div><div class="stat-label">DAYS TO<br>PLACEMENT</div></div>
  <div class="abs stat" style="top:846px"><div class="stat-badge">##</div><div class="stat-label">RETENTION RATE<small>(over two yrs)</small></div></div>
  <div class="abs stat" style="top:893px"><div class="stat-badge">##</div><div class="stat-label">YEARS OF TOTAL<br>EXPERIENCE<small>in executive search sector</small></div></div>

  <h2 class="abs heading" style="left:50px;top:957px">Locations</h2>
  <svg class="abs" style="left:52px;top:987px" width="35" height="57" viewBox="0 0 35 57"><path d="M17.5 0C7.8 0 0 7.8 0 17.5 0 28 17.5 57 17.5 57S35 28 35 17.5C35 7.8 27.2 0 17.5 0z" fill="#1a98b4"/><circle cx="17.5" cy="16.5" r="9" fill="#fff"/></svg>
  <p class="abs cities">Hamburg<br>Wien<br>Munchen<br>Dusseldorf</p>

  <!-- Right column -->
  <h2 class="abs heading" style="left:307px;top:199px">Services</h2>
  <h3 class="abs sub" style="left:307px;top:229px">EXECUTIVE SEARCH</h3>
  <p class="abs body" style="left:307px;top:249px;width:520px">We are helping you to identify and hire highly qualified and experienced candidates for senior-level executive positions. Our goal is to identify the most qualified candidates and match them with the needs and culture of your company.</p>
  <h3 class="abs sub" style="left:307px;top:314px">LEADERSHIP ADVISORY</h3>
  <p class="abs body" style="left:307px;top:334px;width:520px">Our Leadership advisory services are for Management Teams as well as HR-Professionals and candidates. They are designed to help you, and your organization, to build strong and effective leadership skills and teams that can drive growth, innovation, and success.</p>

  <div class="abs values">HONEST. PERSONAL. PRAGMATIC. DIVERSE.</div>

  <h2 class="abs heading" style="left:308px;top:507px">Why us?</h2>
  <ul class="abs why">
    <li>Longstanding experience with a passion for placing C-Level Executives</li>
    <li>We work with you personally &amp; act as an ambassador for our clients in the market</li>
    <li>Engaging in at eye-level discussion beyond just placement and HR topics</li>
    <li>Structured, lean and, most importantly, transparent digital processes, with the opportunity of 24/7 self-update on search status in our online tool</li>
    <li>Creative search approaches and comprehensive candidate evaluation</li>
    <li>Through referencing of candidates as part of the process; psychometrics on demand</li>
  </ul>

  <h2 class="abs heading" style="left:308px;top:719px">Recruitment process</h2>

  <div class="abs step" style="left:309px">
    <div class="step-head" style="background:var(--sky)">RESEARCH /<br>LONGLIST</div>
    <div class="step-num">1</div>
    <div class="step-body">
      <b>KICKOFF</b><p>Abstimmung Profil, Positions-beschreibung und Zielfirmen-liste</p>
      <b>RESEARCH</b><p>Aktiver und passive Research, Ansprache pot. Kandidat*innen</p>
    </div>
  </div>
  <div class="abs step" style="left:474px">
    <div class="step-head" style="background:#2c8ba3">FOKUS &amp; INTERVIEWS//<br>SHORTLIST</div>
    <div class="step-num">2</div>
    <div class="step-body" style="padding-left:16px">
      <b>INTERVIEWS</b><p>Prasentation der priorisierten profile, Klienteninterviews</p>
      <b style="margin-top:10px">REFERENZEN</b><p>Gfg. assessments, Einholen von referenzen</p>
    </div>
  </div>
  <div class="abs step" style="left:635px">
    <div class="step-head" style="background:var(--petrol)">ABSCHULSS</div>
    <div class="step-num">3</div>
    <div class="step-body" style="padding-left:18px">
      <b>KANDIDATENAUSWAHL</b><p>Vertragsverhandlung und onboarding, Feedback-Gesprach</p>
    </div>
  </div>

  <h2 class="abs heading" style="left:308px;top:957px">Track record</h2>
  <p class="abs track">Placehoder text - Lorem ipsum dolor sit amet, consectetuer adipiscing elit, sed diam nonummy nibh euismod tincidunt ut laoreet dolore magna aliquam erat volutpat. Ut wisi enim ad minim veniam, quis nostrud exerci Lorem ipsum dolor sit amet, consec-tetuer adipiscing elit, sed diam nonummy nibh euismod tincidunt ut laoreet dolore</p>

  <!-- Footer -->
  <div class="abs footer"></div>
  <p class="abs cta">LET’S WORK<br>TOGETHER</p>
  <div class="abs contact" style="top:1077px">
    <svg viewBox="0 0 20 20"><circle cx="10" cy="10" r="9" fill="none" stroke="#fff" stroke-width="1.2"/><ellipse cx="10" cy="10" rx="4" ry="9" fill="none" stroke="#fff" stroke-width="1"/><path d="M1 10h18M3 5.5h14M3 14.5h14" stroke="#fff" stroke-width="1"/></svg>
    <span>www.silverpinexs.io</span>
  </div>
  <div class="abs contact" style="top:1101px">
    <svg viewBox="0 0 20 20"><circle cx="10" cy="10" r="9" fill="none" stroke="#fff" stroke-width="1.2"/><rect x="5" y="6.5" width="10" height="7" fill="none" stroke="#fff" stroke-width="1"/><path d="M5 6.5l5 4 5-4" fill="none" stroke="#fff" stroke-width="1"/></svg>
    <span>office@silverpinexs.io</span>
  </div>
  <div class="abs contact" style="top:1125px">
    <svg viewBox="0 0 20 20"><circle cx="10" cy="10" r="9" fill="#fff"/><rect x="7" y="4.5" width="6" height="11" rx="1.2" fill="none" stroke="#56b1c9" stroke-width="1.2"/></svg>
    <span>040 555/0192</span>
  </div>
  <div class="abs social" style="left:532px"></div>
  <div class="abs social" style="left:571px"></div>
  <div class="abs social" style="left:610px"></div>
  <div class="abs badge">Silverpine</div>

</div>
</body>
</html>
```